flyer for letter box drop 2012

Advertising flyer that is delivered to homes in our suburb.
We are optometrists and looking to have a flyer delivered into our local area residential letterboxes. As a business that has been in the area for 25 years we are looking for an innovative approach to keeping our existing customers as well as appealing to the new generation.
We would like the flyer to reflect or professional eye care services
and commitment to quality service and products.
We do not promote our selves as a discount outlet for eg 2 for 1,50% of everything.
I have attached a copy of the flyer we have been using for the last 12 months.

Reason: Away for 3 days

Reason: advertising manager on leave for 7 days, still to review designs

25- 70 year olds male and female

Residential

• flyer should be double sided a5 page
Prominent logo display
address ,phone number , web address,

```html
<!DOCTYPE html>
<html lang="en">
<head>
<meta charset="utf-8">
<title>Carrow Lane Optical – Letterbox Flyer</title>
<link href="https://fonts.googleapis.com/css2?family=Source+Sans+3:wght@400;600;700&display=swap" rel="stylesheet">
<style>
  :root {
    --bg: #e4e2df;
    --navy: #2a3f8f;
    --blue-light: #3189d6;
    --blue-dark: #1a5aa8;
    --orange: #f28c1e;
    --ink: #2b2b2b;
    --ink-soft: #555;
    --paper: #ffffff;
    --paper-grey: #f2f2f2;
    --rule: #cfcfcf;
    --rule-light: rgba(255,255,255,0.45);
  }
  * { box-sizing: border-box; margin: 0; padding: 0; }
  html, body { width: 1200px; height: 900px; overflow: hidden; }
  body {
    background: var(--bg);
    font-family: "Source Sans 3", "Helvetica Neue", Arial, sans-serif;
    color: var(--ink);
    position: relative;
  }
  .flyer {
    position: absolute;
    top: 50px;
    width: 566px;
    height: 800px;
    background: var(--paper);
    overflow: hidden;
    box-shadow: 0 4px 18px rgba(0,0,0,0.18);
  }
  .flyer--front { left: 20px; }
  .flyer--back { left: 614px; }

  /* ---------- front ---------- */
  .hero-photo {
    position: absolute; left: 0; top: 0; width: 566px; height: 360px;
    background: linear-gradient(100deg, #d9b8a0 0%, #c99c80 18%, #eceff2 44%, #f7f8f9 100%);
  }
  .brand {
    position: absolute; left: 300px; top: 92px;
    color: var(--navy); font-weight: 600; line-height: 1;
  }
  .brand__line1 { font-size: 32px; letter-spacing: -0.3px; }
  .brand__line2 { font-size: 50px; margin-top: 4px; letter-spacing: -0.5px; }

  .info-panel {
    position: absolute; left: 262px; top: 300px; width: 304px; height: 500px;
    background: linear-gradient(180deg, var(--blue-light), var(--blue-dark));
    color: #fff; padding: 22px 22px 0 20px;
  }
  .info-panel__title { font-size: 20px; font-weight: 700; }
  .info-panel__sub { font-size: 14px; margin: 2px 0 0 34px; }
  .services { list-style: none; margin-top: 16px; border-top: 1px solid var(--rule-light); }
  .services li {
    font-size: 12.5px; font-weight: 600; padding: 8px 0;
    border-bottom: 1px solid var(--rule-light); line-height: 1.25;
  }
  .services li::before { content: "· "; }
  .staff__title { font-size: 18px; font-weight: 700; margin-top: 22px; }
  .staff__names { font-size: 13px; margin: 6px 0 0 16px; }
  .staff__names span { margin: 0 10px; }
  .staff__text { font-size: 11.5px; line-height: 1.35; margin-top: 16px; padding-bottom: 14px; border-bottom: 1px solid var(--rule-light); }
  .visit { position: absolute; left: 20px; bottom: 34px; }
  .visit__cta { font-size: 14px; font-weight: 700; }
  .visit__web { font-size: 15px; margin-top: 4px; }

  .exam-col {
    position: absolute; left: 0; top: 360px; width: 262px; height: 440px;
    background: var(--paper-grey); padding: 22px 18px 0 20px;
  }
  .exam-col__head { display: flex; align-items: flex-start; gap: 10px; }
  .arrow-box {
    flex: none; width: 24px; height: 24px; background: var(--orange);
    display: flex; align-items: center; justify-content: center;
  }
  .exam-col__title { font-size: 14.5px; font-weight: 700; line-height: 1.2; }
  .checks { list-style: none; margin-top: 18px; }
  .checks li { font-size: 13px; color: var(--ink-soft); line-height: 1.6; }
  .checks li::before { content: "· "; }
  .exam-col__staff { font-size: 12.5px; font-weight: 700; line-height: 1.35; margin-top: 28px; padding-bottom: 18px; border-bottom: 1px solid var(--rule); }
  .contact { margin-top: 18px; font-size: 12px; color: var(--ink-soft); }
  .contact dt { font-weight: 700; color: var(--ink); }
  .contact dd { margin-bottom: 10px; }

  /* ---------- back ---------- */
  .frames-photo {
    position: absolute; left: 0; top: 0; width: 270px; height: 800px;
    background: linear-gradient(160deg, #f4f6f8 0%, #d6dbe0 35%, #eef0f2 60%, #c9ced4 100%);
  }
  .faq-panel {
    position: absolute; left: 270px; top: 0; width: 296px; height: 800px;
    background: linear-gradient(180deg, var(--blue-light), var(--blue-dark));
    color: #fff; padding: 36px 22px 0 22px;
  }
  .faq-panel__title { font-size: 21px; font-weight: 700; }
  .faq-panel__sub { font-size: 14px; margin-bottom: 10px; }
  .faq { margin-top: 22px; }
  .faq__q { display: flex; gap: 10px; font-size: 14.5px; font-weight: 700; line-height: 1.2; }
  .faq__q .arrow-box { background: #fff; width: 20px; height: 20px; }
  .faq__a { font-size: 11.5px; line-height: 1.4; margin: 10px 0 0 30px; padding-bottom: 24px; border-bottom: 1px solid var(--rule-light); }
  .faq:last-of-type .faq__a { border-bottom: none; }
  .back-contact {
    position: absolute; left: 22px; right: 22px; bottom: 40px;
    border-top: 1px solid var(--rule-light); padding-top: 16px; font-size: 12px;
  }
  .back-contact__row { display: flex; gap: 26px; margin-bottom: 12px; }
  .back-contact strong { display: block; font-weight: 700; font-size: 12.5px; }
  .back-contact__web { font-size: 14px; }
</style>
</head>
<body>

<section class="flyer flyer--front">
  <div class="hero-photo" role="img" aria-label="Smiling woman adjusting her glasses in front of an eye chart"></div>
  <div class="brand">
    <div class="brand__line1">Carrow Lane</div>
    <div class="brand__line2">Optical</div>
  </div>

  <div class="exam-col">
    <div class="exam-col__head">
      <span class="arrow-box"><svg width="12" height="12" viewBox="0 0 12 12"><polyline points="3,1 9,6 3,11" fill="none" stroke="#fff" stroke-width="2.4"/></svg></span>
      <h2 class="exam-col__title">Healthcare bulk billed eye examination</h2>
    </div>
    <ul class="checks">
      <li>Glaucoma assessment</li>
      <li>Diabetes vision assessment</li>
      <li>Cataract assessment</li>
      <li>Macula degeneration assessment</li>
      <li>Retinal photography</li>
    </ul>
    <p class="exam-col__staff">Qualified and experienced Optometrist and Optical Technician in store</p>
    <dl class="contact">
      <dt>Address</dt><dd>14b Carrow Lane, Northfield</dd>
      <dt>Phone</dt><dd>9000 4821</dd>
    </dl>
  </div>

  <div class="info-panel">
    <h2 class="info-panel__title">Independent Optometrists</h2>
    <p class="info-panel__sub">Servicing Northfield since 1989</p>
    <ul class="services">
      <li>Latest spectacle and contact lenses</li>
      <li>Direct billing to private health funds with ClaimPoint</li>
      <li>On site lens fittings to own frames</li>
    </ul>
    <h3 class="staff__title">Optometrists:</h3>
    <p class="staff__names">Peter Lindqvist<span>|</span>Maria Oduya</p>
    <p class="staff__text">Our optometrists are experts in eye health, visual correction and the prescribing of optical lenses. They examine your eyes to assess, diagnose and manage ocular diseases, injuries or disorders.</p>
    <div class="visit">
      <p class="visit__cta">Visit us for more information!</p>
      <p class="visit__web">www.carrowlaneoptical.com.au</p>
    </div>
  </div>
</section>

<section class="flyer flyer--back">
  <div class="frames-photo" role="img" aria-label="Assorted spectacle frames lying on an eye chart"></div>
  <div class="faq-panel">
    <h2 class="faq-panel__title">Frequently Asked Questions</h2>
    <p class="faq-panel__sub">Let us answer you</p>

    <div class="faq">
      <h3 class="faq__q"><span class="arrow-box"><svg width="10" height="10" viewBox="0 0 12 12"><polyline points="3,1 9,6 3,11" fill="none" stroke="#1f6ab8" stroke-width="2.6"/></svg></span>Do all optical outlets sell the same spectacle lenses?</h3>
      <p class="faq__a">No. Advances in modern technology have allowed the introduction of new spectacle lens designs which offer better vision. At Carrow Lane Optical we choose value lenses based on their ability to best enhance your sight.</p>
    </div>

    <div class="faq">
      <h3 class="faq__q"><span class="arrow-box"><svg width="10" height="10" viewBox="0 0 12 12"><polyline points="3,1 9,6 3,11" fill="none" stroke="#1f6ab8" stroke-width="2.6"/></svg></span>If I want new prescription lenses fitted to my existing pair of glasses, do I have to go without them for a week?</h3>
      <p class="faq__a">No. This is not the case at Carrow Lane Optical. New lenses can be fitted onsite within 1 hour.</p>
    </div>

    <div class="faq">
      <h3 class="faq__q"><span class="arrow-box"><svg width="10" height="10" viewBox="0 0 12 12"><polyline points="3,1 9,6 3,11" fill="none" stroke="#1f6ab8" stroke-width="2.6"/></svg></span>Do I have to purchase my spectacles where my private health fund directs?</h3>
      <p class="faq__a">No. It is your decision where to have your eyes tested and where to purchase your spectacles or contact lenses. We can direct bill your private health fund with the ClaimPoint system.</p>
    </div>

    <div class="back-contact">
      <div class="back-contact__row">
        <div><strong>Phone</strong>9000 4821</div>
        <div><strong>Address</strong>14b Carrow Lane, Northfield</div>
      </div>
      <strong>Website</strong>
      <span class="back-contact__web">www.carrowlaneoptical.com.au</span>
    </div>
  </div>
</section>

</body>
</html>
```